Business Card Design

I'm a commercial general contractor remodel offices, hotels, health clubs and stores mostly San Francisco and the peninsula
the file I down loaded is kind of what I want I like the I beam with my company name in it, that would be fine with me but if you have better Idea will look at it you never know, I'm decided to give in and change my company name to how every one knows me, I have been in business since 1991, I like the I beam logo I included one of my old card from my old company for reference for you.

Industry/Entity Type

Business

Contact Information for Business Card

BRAXO CONSTRUCTION (is my company name)
Wendell Trusk contractor, LIc 314827
4158 Garnet Row, San Bruno, California 94066
mobile, (415) 555-0147
phone (650) 555-0182
Fax, (650) 555-0183
email, braxo@braxoconstruction.example

```html
<!DOCTYPE html>
<html lang="en">
<head>
<meta charset="utf-8">
<title>Wendell Trusk – Business Card</title>
<link rel="stylesheet" href="https://fonts.googleapis.com/css2?family=Open+Sans:wght@400;600;700&display=swap">
<style>
  :root {
    --band-grey: #a3bdc3;
    --card-blue: #1ca6fd;
    --ink-dark: #1c3440;
    --ink-light: #ffffff;
  }
  html, body {
    margin: 0;
    padding: 0;
    overflow: hidden;
    background: #ffffff;
  }
  .card {
    position: relative;
    width: 1200px;
    height: 702px;
    background: var(--card-blue);
    font-family: "Open Sans", "Segoe UI", sans-serif;
    overflow: hidden;
  }
  .card__header {
    position: absolute;
    left: 0;
    top: 0;
    width: 1200px;
    height: 242px;
    background: var(--band-grey);
  }
  .brand {
    position: absolute;
    left: 0;
    width: 1200px;
    top: 84px;
    text-align: center;
    font-size: 40px;
    font-weight: 700;
    line-height: 1;
    letter-spacing: 1px;
    color: var(--ink-dark);
  }
  .address {
    position: absolute;
    left: 0;
    width: 1200px;
    top: 189px;
    text-align: center;
    font-size: 24px;
    font-weight: 400;
    line-height: 1.2;
    color: var(--ink-dark);
  }
  .person {
    position: absolute;
    left: 0;
    width: 1200px;
    top: 300px;
    text-align: center;
    color: var(--ink-light);
  }
  .person__name {
    margin: 0;
    font-size: 70px;
    font-weight: 700;
    line-height: 1.1;
  }
  .person__role {
    margin: 0;
    font-size: 37px;
    font-weight: 700;
    line-height: 1.15;
  }
  .contact {
    position: absolute;
    left: 0;
    width: 1200px;
    top: 460px;
    text-align: center;
    color: var(--ink-light);
    font-size: 35px;
    line-height: 45px;
  }
  .contact__line {
    margin: 0;
  }
  .contact__email {
    font-weight: 700;
  }
</style>
</head>
<body>
  <div class="card">
    <header class="card__header">
      <div class="brand">BRAXO CONSTRUCTION</div>
      <div class="address">4158 Garnet Row, San Bruno, California 94066</div>
    </header>

    <section class="person">
      <h1 class="person__name">Wendell Trusk</h1>
      <p class="person__role">Contractor, Lic 314827</p>
    </section>

    <section class="contact">
      <p class="contact__line">mobile: (415) 555-0147</p>
      <p class="contact__line">phone: (650) 555-0182 ; Fax: (650) 555-0183</p>
      <p class="contact__line contact__email">braxo@braxoconstruction.example</p>
    </section>
  </div>
</body>
</html>
```